Norvell Earthworks - Civil Construction Construction Company (Telecommunications)

Need a basic website to refine our branding to a current reflection of our service offerings. Norvell Earthworks provides civil construction services specializing in telecommunication sector.
I have started to create a website using word press. I would like to have someone refine the design and polish the overall look and functionality of the site. I would like to website to function in the wordpress format to allow for future edits and control of site.
Included site preview:
https://qmpages-lo.pagebuilderhubsample.net/7e2f90ad.net/Panel/home.html/pv_draft_view

```html
<!DOCTYPE html>
<html lang="en">
<head>
<meta charset="utf-8">
<title>Norvell Earthworks — Website Design</title>
<link href="https://fonts.googleapis.com/css2?family=Russo+One&family=Montserrat:wght@400;500;600&display=swap" rel="stylesheet">
<style>
:root{
  --ink:#1a1a1a;
  --black:#0d0d0d;
  --red:#e31e24;
  --grey:#cfcfcf;
  --card:#4a4a4a;
  --white:#ffffff;
  --text:#555555;
}
*{box-sizing:border-box;margin:0;padding:0}
html,body{width:1200px;height:3529px;overflow:hidden;background:var(--white)}
body{position:relative;font-family:"Montserrat",sans-serif;color:var(--ink)}
.abs{position:absolute}
.brand{font-family:"Russo One",sans-serif;color:var(--ink);white-space:nowrap;display:flex;align-items:center;gap:10px}
.brand .mark{display:inline-block;background:var(--red)}
.head-title{font-family:"Russo One",sans-serif;color:var(--red);letter-spacing:1px}

/* board header */
.board-logo{left:241px;top:76px;font-size:26px}
.board-logo .mark{width:18px;height:18px}
.board-divider{width:1px;height:52px;background:#ddd;top:70px}
.board-label{font-size:14px;font-weight:600;color:var(--ink)}
.board-value{font-size:14px;color:var(--ink)}
.swatches{left:841px;top:97px;display:flex;gap:9px}
.swatches span{width:22px;height:22px;border-radius:4px;display:block}

/* flat screen previews */
.screen{background:var(--white);overflow:hidden;box-shadow:0 0 0 1px #e2e2e2}
.mock-bar{height:17%;background:var(--white);display:flex;align-items:center;padding:0 6%}
.mock-bar .brand{font-size:9px;gap:4px}
.mock-bar .brand .mark{width:6px;height:6px}
.mock-hero{width:100%;height:65%;background:linear-gradient(160deg,#3a3a24,#1d2418 60%,#2a2410);display:flex;flex-direction:column;align-items:center;justify-content:center;text-align:center;padding:0 12%}
.mock-hero b{font-family:"Russo One",sans-serif;color:var(--red);font-weight:400;white-space:nowrap}
.mock-hero i{font-style:normal;color:var(--white);line-height:1.3}
.mock-band{height:8%;background:var(--red);clip-path:polygon(0 0,100% 0,100% 100%,0 30%)}

/* page */
.page{left:142px;top:644px;width:923px;height:2863px;background:var(--white);box-shadow:0 0 6px rgba(0,0,0,.12);overflow:hidden}
.nav-logo{left:67px;top:17px;font-size:27px}
.nav-logo .mark{width:18px;height:18px}
.nav-phone{left:605px;top:14px;font-size:13px;font-weight:600;display:flex;align-items:center;gap:8px}
.btn-outline{border:1.5px solid var(--red);color:var(--red);border-radius:20px;font-size:12px;display:flex;align-items:center;justify-content:center;text-transform:uppercase}
.nav-cta{left:744px;top:8px;width:109px;height:27px}
.nav-links{top:48px;font-size:11.5px;font-weight:600}
.nav-links.active{color:var(--red);border-bottom:1.5px solid var(--red);padding-bottom:2px}

.page-hero{left:0;top:75px;width:923px;height:432px;background:radial-gradient(ellipse at 60% 60%,#4b4520 0%,#2b2e1a 45%,#151a12 100%)}
.hero-title{left:0;top:130px;width:923px;text-align:center;font-size:37px}
.hero-sub{left:170px;top:170px;width:583px;text-align:center;color:var(--white);font-size:21px;line-height:27px;font-weight:500;letter-spacing:.5px}
.hero-btn{left:394px;top:280px;width:134px;height:28px;border:1.5px solid var(--white);color:var(--white);border-radius:16px;font-size:11.5px;display:flex;align-items:center;justify-content:center}
.dots{left:0;top:410px;width:923px;display:flex;justify-content:center;gap:4px}
.dots span{width:11px;height:11px;border:1.5px solid var(--white);border-radius:50%}
.dots span.on{background:var(--red);border-color:var(--red);box-shadow:inset 0 0 0 2px #222}

.photo{background:linear-gradient(150deg,#6b6f4a,#b3351f 55%,#3b2a20)}
.profile-frame{left:68px;top:600px;width:265px;height:433px;border:1.5px solid var(--red)}
.profile-main{left:80px;top:612px;width:241px;height:408px}
.profile-video{left:253px;top:760px;width:202px;height:229px;border:5px solid var(--white);background:linear-gradient(140deg,#506a3a,#c9361e 60%,#2b2b2b)}
.play{left:324px;top:846px;width:54px;height:54px;border-radius:50%;background:var(--white);display:flex;align-items:center;justify-content:center}
.profile-title{left:510px;top:630px;font-size:27px}
.profile-copy{left:510px;top:676px;width:352px;font-size:9.2px;line-height:14.6px;color:var(--text)}
.profile-copy p{margin-bottom:14.5px}
.profile-btn{left:510px;top:956px;width:110px;height:28px}

.why-red{left:473px;top:1094px;width:450px;height:439px;background:linear-gradient(160deg,#e31e24,#d11a20 60%,#c8191f)}
.why-dark{left:0;top:1156px;width:652px;height:433px;background:linear-gradient(180deg,#111 0%,#1a1a1a 60%,#0a0a0a)}
.why-title{left:67px;top:1218px;font-size:25px}
.why-card{top:1274px;width:246px;height:203px;border:1px solid #5a5a5a;padding:58px 18px 0 18px}
.why-card.active{background:var(--card);border-color:var(--card)}
.why-card.on-red{border-color:rgba(255,255,255,.5)}
.why-card svg.icon{position:absolute;left:26px;top:20px}
.why-card ul{list-style:none;color:var(--white);font-size:10.5px;line-height:14px;font-weight:500}
.why-card li{position:relative;padding-left:18px;margin-bottom:7px}
.why-card li::before{content:"";position:absolute;left:0;top:2px;width:9px;height:9px;border-radius:50%;background:var(--red)}
.why-card.on-red li::before{background:var(--white)}
.why-card li::after{content:"";position:absolute;left:2px;top:5px;width:3px;height:3px;border-top:1.2px solid var(--white);border-right:1.2px solid var(--white);transform:rotate(45deg)}
.why-card.on-red li::after{border-color:var(--red)}

.work-title{left:0;top:1660px;width:923px;text-align:center;font-size:25px}
.work-a{left:67px;top:1721px;width:382px;height:153px;background:linear-gradient(160deg,#8a9a4e,#c9a21c 50%,#3e5b20)}
.work-b{left:67px;top:1900px;width:178px;height:154px}
.work-c{left:270px;top:1900px;width:179px;height:154px;background:linear-gradient(160deg,#d7584a,#e4716a);display:flex;align-items:center;justify-content:center}
.work-c .inner{position:absolute;inset:9px;border:1px solid rgba(255,255,255,.6)}
.work-d{left:473px;top:1721px;width:382px;height:333px;background:linear-gradient(180deg,#6fa3df 0%,#b9d3ee 45%,#c32a1c 60%,#3a2f2b 100%)}
.btn-solid{background:var(--red);color:var(--white);border-radius:16px;font-size:11.5px;display:flex;align-items:center;justify-content:center;font-weight:500}
.work-btn{left:405px;top:2099px;width:110px;height:28px}

.inquiry{left:67px;top:2191px;width:788px;height:308px;background:var(--grey)}
.inquiry-title{left:0;top:52px;width:788px;text-align:center;font-size:25px}
.field{background:var(--white);font-size:10px;color:#888;padding:0 12px;display:flex;align-items:center}
.inquiry-btn{left:339px;top:230px;width:110px;height:29px}

.footer-logo{left:0;top:2555px;width:923px;justify-content:center;font-size:31px;color:var(--white)}
.footer-logo .mark{width:20px;height:20px}
.foot-head{font-family:"Russo One",sans-serif;color:var(--red);font-size:13px;letter-spacing:.5px}
.foot-small{font-size:10px;color:var(--red)}
.foot-text{font-size:11.5px;color:var(--white)}
.foot-links{left:319px;top:2670px;list-style:none;font-size:11px;color:var(--white);line-height:20.5px}
.foot-links li:first-child{color:var(--red);text-decoration:underline}
.map{left:491px;top:2637px;width:286px;height:141px;background:linear-gradient(135deg,#eef0ec,#dfe6dc 50%,#e9ece7);border:2px solid #fff}
.social{left:824px;width:29px;height:29px;border-radius:50%;background:#333}
.social.on{background:var(--red)}
.copyright{left:67px;top:2812px;font-size:8.5px;color:var(--white)}
.copyright span{color:var(--red)}
</style>
</head>
<body>

<!-- board header -->
<div class="abs brand board-logo"><span class="mark"></span>NORVELL EARTHWORKS</div>
<div class="abs board-divider" style="left:584px"></div>
<div class="abs board-label" style="left:631px;top:78px">Fonts:</div>
<div class="abs board-value" style="left:631px;top:99px">Russo One, Izmir</div>
<div class="abs board-divider" style="left:792px"></div>
<div class="abs board-label" style="left:841px;top:72px">Colors:</div>
<div class="abs swatches">
  <span style="background:var(--ink)"></span>
  <span style="background:var(--red)"></span>
  <span style="background:var(--grey)"></span>
  <span style="background:var(--white);box-shadow:0 0 0 1px #e5e5e5"></span>
</div>

<!-- flat screen previews -->
<div class="abs screen" style="left:502px;top:205px;width:420px;height:233px">
  <div class="mock-bar"><div class="brand"><span class="mark"></span>NORVELL EARTHWORKS</div></div>
  <div class="mock-hero" role="img" aria-label="Trenching machine on a job site"><b style="font-size:14px">NORVELL EARTHWORKS</b><i style="font-size:8px;margin-top:3px">is a safety conscious, productive and efficient construction firm capable of all facets of civil construction</i></div>
  <div class="mock-band"></div>
</div>
<div class="abs screen" style="left:200px;top:325px;width:318px;height:216px">
  <div class="mock-bar"><div class="brand"><span class="mark"></span>NORVELL EARTHWORKS</div></div>
  <div class="mock-hero" role="img" aria-label="Trenching machine on a job site"><b style="font-size:12px">NORVELL EARTHWORKS</b><i style="font-size:7px;margin-top:3px">is a safety conscious, productive and efficient construction firm capable of all facets of civil construction</i></div>
  <div class="mock-band"></div>
</div>
<div class="abs screen" style="left:922px;top:325px;width:104px;height:218px">
  <div class="mock-bar" style="height:12%"><div class="brand" style="font-size:6px"><span class="mark"></span>NORVELL</div></div>
  <div class="mock-hero" style="height:30%;padding:0 4%" role="img" aria-label="Trenching machine on a job site"><b style="font-size:6px">NORVELL EARTHWORKS</b></div>
  <div style="height:10%;background:var(--red)"></div>
  <div class="head-title" style="font-size:6px;padding:6px">COMPANY PROFILE</div>
  <div class="photo" style="margin:0 8px;height:70px" role="img" aria-label="Red drilling rig"></div>
</div>

<!-- website page -->
<main class="abs page">
  <header>
    <div class="abs brand nav-logo"><span class="mark"></span>NORVELL EARTHWORKS</div>
    <div class="abs nav-phone">
      <svg width="14" height="14" viewBox="0 0 24 24" fill="none" stroke="#e31e24" stroke-width="2"><path d="M5 3h4l2 5-3 2a11 11 0 0 0 6 6l2-3 5 2v4a2 2 0 0 1-2 2A18 18 0 0 1 3 5a2 2 0 0 1 2-2z"/></svg>
      1 (555) 014-2270
    </div>
    <div class="abs btn-outline nav-cta">Contact Us</div>
    <div class="abs nav-links active" style="left:503px">Home</div>
    <div class="abs nav-links" style="left:564px">Company Profile</div>
    <div class="abs nav-links" style="left:684px">Why Choose Us</div>
    <div class="abs nav-links" style="left:801px">Our Work</div>
  </header>

  <section class="abs page-hero" role="img" aria-label="Yellow trenching machine laying red conduit on a grassy site">
    <h1 class="abs head-title hero-title" style="font-weight:400">NORVELL EARTHWORKS</h1>
    <p class="abs hero-sub">is a safety conscious, productive and efficient construction firm capable of all facets of civil construction</p>
    <div class="abs hero-btn">VIEW PROJECTS</div>
    <div class="abs dots"><span></span><span class="on"></span><span></span><span></span></div>
  </section>
  <svg class="abs" style="left:0;top:507px" width="923" height="50" viewBox="0 0 923 50"><polygon points="0,0 923,0 923,50 0,13" fill="#e31e24"/></svg>

  <section>
    <div class="abs profile-frame"></div>
    <div class="abs photo profile-main" role="img" aria-label="Crew member in high-visibility gear operating a red drilling rig"></div>
    <div class="abs profile-video" role="img" aria-label="Red tracked machine on a job site, video thumbnail"></div>
    <div class="abs play"><svg width="20" height="22" viewBox="0 0 20 22"><polygon points="3,0 20,11 3,22" fill="#e31e24"/></svg></div>
    <h2 class="abs head-title profile-title" style="font-weight:400">COMPANY PROFILE</h2>
    <div class="abs profile-copy">
      <p>Norvell Earthworks is a safety conscious, productive and efficient construction firm capable of all facets of civil construction. We have completed thousands of projects across Alberta, Saskatchewan and British Columbia working within various industry sectors. We have built a diverse team of skilled professionals who take a great deal of pride in their work and aim to achieve the highest levels of customer satisfaction.</p>
      <p>"At Norvell Earthworks we strive to provide creative solutions, on-time, on-budget and beyond expectations"</p>
      <p>Each of Norvell's construction crews are dispatched with a full complement of late model equipment and tools required to complete civil underground construction projects in a safe and efficient manner meeting all criteria established by client, governing bodies and site environments. We constantly maintain and update our fleet to supply our clients with the most effective and modern construction solutions possible. Our dedicated maintenance team ensures we are compliant across our wide areas of operation.</p>
    </div>
    <div class="abs btn-outline profile-btn">About Us</div>
  </section>

  <section>
    <div class="abs why-red" role="img" aria-label="Faint photo of a field worker in safety gear under a red tint"></div>
    <div class="abs why-dark" role="img" aria-label="Dark photo of heavy equipment"></div>
    <h2 class="abs head-title why-title" style="font-weight:400">WHY CHOOSE US</h2>
    <div class="abs why-card" style="left:67px">
      <svg class="icon" width="40" height="40" viewBox="0 0 40 40" fill="none" stroke="#fff" stroke-width="1.6"><path d="M10 15a10 10 0 0 1 20 0z"/><path d="M7 15h26"/><circle cx="20" cy="21" r="5"/><path d="M8 38c0-7 5-11 12-11s12 4 12 11"/><circle cx="30" cy="33" r="5"/><path d="M28 33l2 2 3-4"/></svg>
      <ul><li>Accredited health and safety program</li><li>Proven track record of safety excellence</li><li>Continuous training and development of employees</li></ul>
    </div>
    <div class="abs why-card active" style="left:338px">
      <svg class="icon" width="40" height="40" viewBox="0 0 40 40" fill="none" stroke="#fff" stroke-width="1.6"><circle cx="20" cy="20" r="16"/><circle cx="20" cy="20" r="10"/><path d="M20 4v6M20 30v6M4 20h6M30 20h6"/><circle cx="20" cy="20" r="3"/></svg>
      <ul><li>Productive and efficient crews</li><li>Current fleet of modern equipment</li><li>Use of latest construction techniques/technologies</li></ul>
    </div>
    <div class="abs why-card on-red" style="left:609px">
      <svg class="icon" width="42" height="40" viewBox="0 0 42 40" fill="none" stroke="#fff" stroke-width="1.6"><path d="M2 16l8-8 8 4 6-2 8 8-8 10-8-4"/><path d="M40 16l-8-8"/><path d="M14 24l4 4M18 20l6 6M22 18l6 6"/></svg>
      <ul><li>Quality and process driven</li><li>Excellent customer service</li><li>Privately owned and operated</li><li>Dependable, Reliable and Honest</li></ul>
    </div>
  </section>

  <section>
    <h2 class="abs head-title work-title" style="font-weight:400">OUR WORK</h2>
    <div class="abs work-a" role="img" aria-label="Yellow trencher with red conduit reel on green grass"></div>
    <div class="abs photo work-b" role="img" aria-label="Red drilling rig beside a tree line"></div>
    <div class="abs work-c" role="img" aria-label="Job site photo under red hover overlay">
      <span class="inner"></span>
      <svg width="22" height="22" viewBox="0 0 22 22" stroke="#fff" stroke-width="1.5"><path d="M11 0v22M0 11h22"/></svg>
    </div>
    <div class="abs work-d" role="img" aria-label="Red tracked machine carrying an orange conduit reel under blue sky"></div>
    <div class="abs btn-solid work-btn">VIEW ALL</div>
  </section>

  <svg class="abs" style="left:0;top:2330px" width="923" height="533" viewBox="0 0 923 533"><polygon points="0,0 67,0 67,20 0,20" fill="#e31e24"/><polygon points="855,0 923,0 923,20 855,20" fill="#e31e24"/><polygon points="0,20 923,20 923,533 0,533" fill="#0d0d0d"/><polygon points="0,8 67,20 0,20" fill="#0d0d0d"/></svg>

  <section class="abs inquiry">
    <h2 class="abs head-title inquiry-title" style="font-weight:400">QUICK INQUIRY</h2>
    <div class="abs field" style="left:92px;top:105px;width:197px;height:29px">Name</div>
    <div class="abs field" style="left:296px;top:105px;width:196px;height:29px">Email</div>
    <div class="abs field" style="left:499px;top:105px;width:196px;height:29px">Phone</div>
    <div class="abs field" style="left:92px;top:141px;width:603px;height:55px;align-items:flex-start;padding-top:10px">Message..</div>
    <div class="abs btn-solid inquiry-btn">SUBMIT</div>
  </section>

  <footer>
    <div class="abs brand footer-logo"><span class="mark"></span>NORVELL EARTHWORKS</div>
    <div class="abs foot-head" style="left:67px;top:2640px">CONTACT US</div>
    <svg class="abs" style="left:67px;top:2666px" width="18" height="18" viewBox="0 0 24 24" fill="none" stroke="#e31e24" stroke-width="1.8"><path d="M5 3h4l2 5-3 2a11 11 0 0 0 6 6l2-3 5 2v4a2 2 0 0 1-2 2A18 18 0 0 1 3 5a2 2 0 0 1 2-2z"/></svg>
    <div class="abs foot-small" style="left:94px;top:2667px">Call</div>
    <div class="abs foot-text" style="left:94px;top:2681px">1 (555) 014-2270</div>
    <svg class="abs" style="left:67px;top:2706px" width="19" height="16" viewBox="0 0 24 18" fill="none" stroke="#e31e24" stroke-width="1.8"><rect x="1" y="1" width="22" height="16"/><path d="M1 1l11 9 11-9"/></svg>
    <div class="abs foot-small" style="left:94px;top:2705px">Email</div>
    <div class="abs foot-text" style="left:94px;top:2719px">info@norvellearthworks.com</div>
    <div class="abs foot-head" style="left:319px;top:2640px">QUICK LINKS</div>
    <ul class="abs foot-links"><li>Home</li><li>About Us</li><li>Services</li><li>Projects</li><li>Contact Us</li></ul>
    <div class="abs map" role="img" aria-label="Street map showing the office location with a red pin"></div>
    <div class="abs social" style="top:2656px"></div>
    <div class="abs social on" style="top:2693px"></div>
    <div class="abs social" style="top:2730px"></div>
    <div class="abs copyright">© 2022 <span>NORVELL EARTHWORKS</span>. ALL RIGHTS RESERVED</div>
  </footer>
</main>

</body>
</html>
```